11 x 11 Flyer Design for Social Media - Reverse Mortgages

62 or older?

A Reverse Mortgage
could be
Your Road to Financial Freedom

* No Monthly Payments
* No Income Requirements
* No Credit Score Requirements
* No Loss of Ownership

Receive cash by lump sum, monthly installments or a line of credit!!

Call us today for a Free Consultation!!
(800) 471-2965

Bluegate Financial Services, Inc.
NMLS #318760
www.bluegatehome.com

```html
<!DOCTYPE html>
<html lang="en">
<head>
<meta charset="utf-8">
<title>62 or Older? – Reverse Mortgage Flyer</title>
<link href="https://fonts.googleapis.com/css2?family=Bebas+Neue&family=Montserrat:wght@400;500;700&display=swap" rel="stylesheet">
<style>
  :root {
    --navy: #1d4e7e;
    --green: #6aab2e;
    --green-dark: #4d8a22;
    --ink: #1f1f1f;
    --white: #ffffff;
    --sky: #eef1f1;
    --sea: #b9c3c6;
    --sand: #d9dbd6;
    --skin: #6b4532;
    --linen: #f4f4f2;
  }
  * { box-sizing: border-box; margin: 0; padding: 0; }
  html, body { width: 800px; height: 1200px; overflow: hidden; background: var(--white); }
  .flyer {
    position: relative; width: 800px; height: 1200px; overflow: hidden;
    background: var(--white); font-family: 'Montserrat', sans-serif; color: var(--ink);
  }
  .hero-photo {
    position: absolute; left: 0; top: 0; width: 800px; height: 520px;
    background:
      radial-gradient(ellipse 70px 60px at 472px 210px, rgba(107,69,50,.85) 0%, rgba(107,69,50,0) 100%),
      radial-gradient(ellipse 70px 70px at 655px 130px, rgba(90,58,42,.85) 0%, rgba(90,58,42,0) 100%),
      radial-gradient(ellipse 110px 210px at 540px 390px, rgba(255,255,255,.95) 0%, rgba(255,255,255,0) 100%),
      radial-gradient(ellipse 120px 240px at 690px 330px, rgba(255,255,255,.95) 0%, rgba(255,255,255,0) 100%),
      linear-gradient(180deg, var(--sky) 0%, #e9eded 28%, var(--sea) 40%, #cfd6d7 50%, #e4e7e5 62%, var(--sand) 80%, #e6e7e3 100%);
  }
  .brand {
    position: absolute; left: 72px; top: 108px;
    display: flex; align-items: center; gap: 14px;
  }
  .brand-dot { width: 40px; height: 40px; border-radius: 50%; background: var(--navy); }
  .brand-name { font-weight: 700; font-size: 22px; color: var(--navy); line-height: 1.2; }
  .headline-band {
    position: absolute; left: 0; top: 514px; width: 505px; height: 150px;
    background: var(--navy); display: flex; align-items: center; padding-left: 30px;
  }
  .headline {
    font-family: 'Bebas Neue', sans-serif; font-weight: 400; font-size: 98px; color: var(--white);
    letter-spacing: 1px; line-height: 1; padding-top: 8px;
  }
  .subhead-band {
    position: absolute; left: 0; top: 664px; width: 520px; height: 72px;
    background: linear-gradient(90deg, var(--green-dark) 0%, var(--green) 70%, rgba(106,171,46,0) 100%);
    padding: 13px 0 0 32px;
  }
  .subhead {
    font-size: 18.5px; font-weight: 500; color: var(--white);
    text-transform: uppercase; line-height: 1.1;
  }
  .benefits { position: absolute; left: 36px; top: 770px; list-style: none; }
  .benefits li {
    display: flex; align-items: center; gap: 12px; height: 35px;
    font-size: 17px; font-weight: 500; text-transform: uppercase;
  }
  .benefits svg { width: 14px; height: 14px; flex: none; }
  .rule { position: absolute; left: 37px; top: 916px; width: 90px; height: 2px; background: var(--ink); }
  .offer {
    position: absolute; left: 37px; top: 938px;
    font-size: 21px; font-weight: 700; line-height: 1.3;
  }
  .cta-band {
    position: absolute; left: 0; top: 1016px; width: 510px; height: 52px;
    background: var(--green); border-radius: 0 26px 26px 0;
    display: flex; align-items: center; padding-left: 30px;
  }
  .cta {
    font-family: 'Bebas Neue', sans-serif; font-size: 34px; color: var(--white);
    letter-spacing: .3px; padding-top: 4px;
  }
  .phone {
    position: absolute; left: 30px; top: 1080px;
    font-size: 42px; font-weight: 700; color: var(--ink);
  }
  .footer-band {
    position: absolute; left: 0; right: 0; bottom: 0; height: 58px;
    background: var(--navy); display: flex; align-items: center; padding-left: 30px;
    color: var(--white); font-size: 16px; font-weight: 500;
  }
  .footer-item { display: flex; align-items: center; gap: 10px; }
  .footer-item svg { width: 30px; height: 30px; }
  .footer-divider { width: 2px; height: 32px; background: var(--white); margin: 0 22px; }
  .photo-circle {
    position: absolute; border-radius: 50%; border: 7px solid var(--white);
    box-shadow: 0 4px 12px rgba(0,0,0,.35);
  }
  .photo-circle.couple-laughing {
    left: 490px; top: 423px; width: 304px; height: 304px;
    background:
      radial-gradient(circle at 35% 30%, #e4e2df 0%, rgba(228,226,223,0) 30%),
      radial-gradient(circle at 60% 45%, #6b4532 0%, rgba(107,69,50,0) 35%),
      linear-gradient(160deg, #8fb6d4 0%, #c9d5dc 40%, #2a3450 100%);
  }
  .photo-circle.couple-car {
    left: 430px; top: 680px; width: 262px; height: 262px;
    background:
      radial-gradient(circle at 40% 35%, #e6e2da 0%, rgba(230,226,218,0) 30%),
      radial-gradient(circle at 70% 50%, #7a5240 0%, rgba(122,82,64,0) 30%),
      linear-gradient(180deg, #9fc3a0 0%, #c8c2b6 40%, #4a4f55 80%, #2c3238 100%);
  }
  .photo-circle.man-thinking {
    left: 578px; top: 874px; width: 188px; height: 188px;
    background:
      radial-gradient(circle at 45% 45%, #7b5440 0%, rgba(123,84,64,0) 40%),
      linear-gradient(180deg, #cfe3ec 0%, #9fc0d3 60%, #e6eef2 100%);
  }
</style>
</head>
<body>
<main class="flyer">
  <div class="hero-photo" role="img" aria-label="Smiling senior couple in white clothes standing arm in arm on a misty beach"></div>

  <div class="brand">
    <span class="brand-dot"></span>
    <span class="brand-name">Bluegate Financial Services, Inc.</span>
  </div>

  <div class="headline-band"><h1 class="headline">62 OR OLDER?</h1></div>
  <div class="subhead-band">
    <p class="subhead">A reverse mortgage could be<br>your road to financial freedom</p>
  </div>

  <div class="photo-circle couple-laughing" role="img" aria-label="Senior couple laughing together cheek to cheek"></div>
  <div class="photo-circle couple-car" role="img" aria-label="Senior couple smiling in a convertible car"></div>
  <div class="photo-circle man-thinking" role="img" aria-label="Senior man resting his chin on his hand in thought"></div>

  <ul class="benefits">
    <li><svg viewBox="0 0 14 14"><path d="M0 0 L14 7 L0 14 L4 7 Z" fill="var(--green)"/><path d="M0 7 L14 7 L0 14 L4 7 Z" fill="var(--navy)"/></svg>No monthly payments</li>
    <li><svg viewBox="0 0 14 14"><path d="M0 0 L14 7 L0 14 L4 7 Z" fill="var(--green)"/><path d="M0 7 L14 7 L0 14 L4 7 Z" fill="var(--navy)"/></svg>No income requirements</li>
    <li><svg viewBox="0 0 14 14"><path d="M0 0 L14 7 L0 14 L4 7 Z" fill="var(--green)"/><path d="M0 7 L14 7 L0 14 L4 7 Z" fill="var(--navy)"/></svg>No credit score requirements</li>
    <li><svg viewBox="0 0 14 14"><path d="M0 0 L14 7 L0 14 L4 7 Z" fill="var(--green)"/><path d="M0 7 L14 7 L0 14 L4 7 Z" fill="var(--navy)"/></svg>No loss of ownership</li>
  </ul>

  <div class="rule"></div>
  <p class="offer">Receive cash by lump sum,<br>monthly installments or a line of credit!!</p>

  <div class="cta-band"><p class="cta">CALL US TODAY FOR A FREE CONSULTATION!!</p></div>
  <p class="phone">Call : (800) 471-2965</p>

  <footer class="footer-band">
    <span class="footer-item">
      <svg viewBox="0 0 30 30"><circle cx="15" cy="15" r="14" fill="var(--white)"/><g fill="none" stroke="var(--navy)" stroke-width="1.6"><circle cx="15" cy="15" r="8"/><ellipse cx="15" cy="15" rx="3.5" ry="8"/><line x1="7" y1="15" x2="23" y2="15"/><line x1="8.5" y1="11" x2="21.5" y2="11"/><line x1="8.5" y1="19" x2="21.5" y2="19"/></g></svg>
      www.bluegatehome.com
    </span>
    <span class="footer-divider"></span>
    <span class="footer-item">
      <svg viewBox="0 0 30 30"><circle cx="15" cy="15" r="14" fill="var(--white)"/><path d="M15 6 a6 6 0 0 1 6 6 c0 4.5 -6 12 -6 12 s-6 -7.5 -6 -12 a6 6 0 0 1 6 -6 z" fill="var(--navy)"/><circle cx="15" cy="12" r="2.3" fill="var(--white)"/></svg>
      Bluegate Financial Services, Inc. NMLS #318760
    </span>
  </footer>
</main>
</body>
</html>
```